Business Card Design Project

Card must be printed on two sides
Preference for horizontal layout
Clean images-easy to understand the offer

Loyalty Card

Buy any Juice/Smoothie/Falafel Pocket - 7th one is free

Emphasis on the 7 and FREE
Updates

Please note: We have added some more information and tried to clarify the offer.
All submissions welcome
We will have further design work to follow up this promotion.

Thank you.

Regards
Dennis

Target Market(s)

Local residents
Many singles
Age: 20-45
Male & Female
Healthy & tasty fresh food and juice - most purchases under $15
We are located close to the seaside in St Kilda Melbourne Victoria

Industry/Entity Type

Business

Requirements
Must have
• QB Logo
Address: 52 Morrow Lane St Kilda Vic 3182

6 Squares/Circles/empty logos to stamp purchases

Limit one use per customer per visit (small text)
Buy any juice/smoothie or whole falafel pocket and you will receive one item of your choice free on your 7th visit.
Offer Valid till: (blank)

Two sided: Logo (optional: Brief about the business) on front and detail on the back
Nice to have
• Design and offer that you will keep not throw away

Images need to be sharp and easy to understand the offer

Not transferable - one per customer

```html
<!DOCTYPE html>
<html lang="en">
<head>
<meta charset="utf-8">
<title>QuayBite Loyalty Card</title>
<link rel="stylesheet" href="https://fonts.googleapis.com/css2?family=Archivo+Black&family=Nunito:wght@400;600;800&display=swap">
<style>
  :root {
    --page: #ecebe6;
    --card-light: #f9fcf3;
    --card-mid: #e2f2d0;
    --card-edge: #c3e3a0;
    --brand-green: #6cc24a;
    --offer-red: #e0262f;
    --fine-green: #6aa84f;
    --art-light: #a9da8a;
    --art-deep: #7cc55a;
    --stamp: #ffffff;
    --stamp-ring: #e6f1d8;
  }
  * { box-sizing: border-box; margin: 0; padding: 0; }
  html, body { width: 1200px; height: 901px; overflow: hidden; }
  body {
    background: var(--page);
    font-family: "Nunito", sans-serif;
    position: relative;
  }
  .card {
    position: absolute;
    width: 540px;
    height: 330px;
    border-radius: 6px;
    overflow: hidden;
    box-shadow: 0 6px 18px rgba(0,0,0,0.18);
    background: radial-gradient(ellipse 80% 90% at 50% 20%, var(--card-light) 0%, var(--card-mid) 55%, var(--card-edge) 100%);
  }
  .card-front { left: 40px; top: 285px; }
  .card-back  { left: 620px; top: 285px; }

  /* Front */
  .brand {
    position: absolute;
    left: 0; right: 0; top: 118px;
    display: flex; align-items: center; justify-content: center; gap: 16px;
  }
  .brand-dot {
    width: 58px; height: 58px; border-radius: 50%;
    background: var(--brand-green);
  }
  .brand-name {
    font-weight: 800; font-size: 64px; line-height: 1;
    color: var(--brand-green); letter-spacing: -1px;
  }
  .address {
    position: absolute; left: 0; right: 0; top: 210px;
    text-align: center;
    font-weight: 800; font-size: 17px; color: var(--offer-red);
  }

  /* Back */
  .drinks-art {
    position: absolute; left: 226px; top: 30px;
    width: 88px; height: 68px; border-radius: 8px;
    background: linear-gradient(160deg, var(--art-light) 0%, var(--art-deep) 100%);
  }
  .offer-lead {
    position: absolute; left: 0; right: 0; top: 108px;
    text-align: center; font-weight: 600; font-size: 15px;
    color: var(--fine-green);
  }
  .offer-headline {
    position: absolute; left: 0; right: 0; top: 128px;
    text-align: center;
    font-family: "Archivo Black", sans-serif;
    font-size: 27px; line-height: 1.2; color: var(--offer-red); letter-spacing: 0.5px;
  }
  .offer-headline sup { font-size: 14px; }
  .stamps { position: absolute; inset: 0; }
  .stamp {
    position: absolute; width: 54px; height: 54px; border-radius: 50%;
    background: var(--stamp);
    box-shadow: inset 0 0 0 4px var(--stamp-ring), 0 1px 3px rgba(0,0,0,0.12);
  }
  .fine-print {
    position: absolute; left: 20px; right: 20px; top: 270px;
    text-align: center; font-size: 11.5px; line-height: 1.45;
    color: var(--fine-green);
  }
</style>
</head>
<body>
  <section class="card card-front" aria-label="Card front">
    <div class="brand">
      <span class="brand-dot"></span>
      <span class="brand-name">QuayBite</span>
    </div>
    <p class="address">Address: 52 Morrow Lane St Kilda Vic 3182</p>
  </section>

  <section class="card card-back" aria-label="Card back">
    <div class="drinks-art" role="img" aria-label="Illustration of a juice cup, a smoothie glass and a falafel pocket"></div>
    <p class="offer-lead">Buy any 6 Juice, Smoothie or Falafel Pocket</p>
    <h1 class="offer-headline">GET YOUR 7<sup>TH</sup> ONE FOR FREE</h1>
    <div class="stamps" aria-label="Six stamp spaces">
      <span class="stamp" style="left:52px;top:200px"></span>
      <span class="stamp" style="left:120px;top:185px"></span>
      <span class="stamp" style="left:188px;top:172px"></span>
      <span class="stamp" style="left:256px;top:172px"></span>
      <span class="stamp" style="left:324px;top:172px"></span>
      <span class="stamp" style="left:392px;top:172px"></span>
    </div>
    <p class="fine-print">Buy any 6 juice/smoothie or whole falafel pocket items and you will receive your 7th item free<br>Limit one use per customer per visit. Offer Valid till: ____________</p>
  </section>
</body>
</html>
```